KORVELTA Corporate Business Card

Modern business card design for company which focuses in the areas of Staffing, IT Consulting & Data Services. Please note: We are no longer using the IT subscript on the logo. All designs should have IT subscript removed.
Website: www.korveltait.example

```html
<!DOCTYPE html>
<html lang="en">
<head>
<meta charset="utf-8">
<title>KORVELTA Business Card</title>
<link rel="stylesheet" href="https://fonts.googleapis.com/css2?family=Arimo:wght@400;700&display=swap">
<style>
  :root {
    --stage-light: #8a8a8a;
    --stage-dark: #555555;
    --card-white: #ffffff;
    --card-dark: #292929;
    --square-dark: #1a1a1a;
    --square-light: #3c3c3c;
    --brand-navy: #075a94;
    --brand-sky: #1b9cd9;
    --text-grey: #4a4a4a;
  }
  * { margin: 0; padding: 0; box-sizing: border-box; }
  html, body { width: 1200px; height: 1200px; overflow: hidden; }
  body {
    background: radial-gradient(circle at 50% 50%, var(--stage-light), var(--stage-dark));
    font-family: "Arimo", Arial, sans-serif;
    position: relative;
  }
  .card {
    position: absolute;
    left: 160px;
    width: 880px;
    height: 500px;
    border-radius: 26px;
    overflow: hidden;
  }
  .card-back { top: 80px; background: var(--card-dark); }
  .card-front { top: 620px; background: var(--card-white); }

  .back-pattern {
    position: absolute;
    inset: 0;
    background:
      radial-gradient(ellipse at 25% 70%, var(--square-dark) 0%, transparent 55%),
      radial-gradient(ellipse at 70% 30%, var(--square-light) 0%, transparent 50%),
      var(--card-dark);
  }
  .back-wordmark {
    position: absolute;
    right: 56px;
    bottom: 48px;
    display: flex;
    align-items: center;
    gap: 16px;
    color: var(--brand-sky);
    font-weight: 700;
    font-size: 70px;
    letter-spacing: 2px;
  }
  .brand-square {
    width: 44px;
    height: 44px;
    background: var(--brand-sky);
  }

  .contact-block {
    position: absolute;
    left: 70px;
    top: 70px;
    color: var(--text-grey);
  }
  .person-name {
    color: var(--brand-navy);
    font-weight: 700;
    font-size: 44px;
    line-height: 1;
  }
  .person-title {
    color: var(--brand-sky);
    font-size: 22px;
    margin-top: 4px;
  }
  .address {
    font-size: 22px;
    line-height: 1.3;
    margin-top: 26px;
  }
  .contact-list {
    list-style: none;
    margin-top: 20px;
    font-size: 22px;
    line-height: 1.5;
  }
  .contact-list li { display: flex; align-items: center; gap: 10px; }
  .contact-list svg { width: 18px; height: 18px; flex: none; }

  .front-wordmark {
    position: absolute;
    right: 70px;
    bottom: 70px;
    display: flex;
    align-items: center;
    gap: 16px;
    color: var(--brand-navy);
    font-weight: 700;
    font-size: 56px;
    letter-spacing: 2px;
  }
  .front-wordmark .brand-square { width: 36px; height: 36px; background: var(--brand-navy); }
</style>
</head>
<body>
  <section class="card card-back">
    <div class="back-pattern" role="img" aria-label="Dark background with scattered shaded squares"></div>
    <div class="back-wordmark"><span class="brand-square"></span>KORVELTA</div>
  </section>

  <section class="card card-front">
    <div class="contact-block">
      <h1 class="person-name">Marten Oakley</h1>
      <p class="person-title">Director</p>
      <p class="address">418 Harlow Ave.<br>Brennick, IN 47000</p>
      <ul class="contact-list">
        <li>
          <svg viewBox="0 0 18 18" aria-hidden="true"><rect x="5" y="1" width="8" height="16" rx="1.5" fill="none" stroke="#075a94" stroke-width="1.8"/><circle cx="9" cy="14" r="1" fill="#075a94"/></svg>
          555-014-2290
        </li>
        <li>
          <svg viewBox="0 0 18 18" aria-hidden="true"><rect x="1" y="4" width="16" height="11" fill="#075a94"/><path d="M1 4 L9 10 L17 4" fill="none" stroke="#fff" stroke-width="1.5"/></svg>
          contactus@korveltait.example
        </li>
        <li>
          <svg viewBox="0 0 18 18" aria-hidden="true"><circle cx="9" cy="9" r="7.5" fill="none" stroke="#075a94" stroke-width="1.6"/><ellipse cx="9" cy="9" rx="3.2" ry="7.5" fill="none" stroke="#075a94" stroke-width="1.3"/><path d="M1.5 9 H16.5 M3 5 H15 M3 13 H15" stroke="#075a94" stroke-width="1.2"/></svg>
          www.korveltait.example
        </li>
      </ul>
    </div>
    <div class="front-wordmark"><span class="brand-square"></span>KORVELTA</div>
  </section>
</body>
</html>
```